Build a Web page - Dovin Pratchell Homes, LLC - a custom home builder

We are a custom home builder in Wisconsin. Need a basic web page with a home page, About Us, Contact info, Gallery, and Testimonials page. Gallery will probably have sub-pages and each will have about ten pictures or less. I already own the domain and have web hosting through Wix, I just need the site built. Once the page is built I should be able to do the upkeep on it myself. If I need to add pictures or whatever.
Updates

Project Deadline Extended
Reason: I am still looking through designs and will select soon - thank you!

Target Market(s)

Gen X and Millennials who are looking to build a home. Custom built homes - not generic spec homes.

Industry/Entity Type

Home Builder

Number of Pages Required

5+ page

Font styles to use
Sans Serif

Colors
ffffff
ec1f27
000000
9d9d9d

Requirements
Must have
• I have no idea if I want coded or in coded. I'm not sure of the difference and why I would want one over the other.
Nice to have
• We like the following colors - red, black, gray, white.
Should not have
• not a big fan of clip art like hammers, tape measures, etc. Must look professional.

```html
<!DOCTYPE html>
<html lang="en">
<head>
<meta charset="utf-8">
<title>Dovin Pratchell Homes – Custom Home Builder</title>
<link href="https://fonts.googleapis.com/css2?family=Jost:wght@400;500&family=Lato:wght@400;700&display=swap" rel="stylesheet">
<style>
:root{
  --red:#9b0f14;
  --red-bar:#a8080d;
  --ink:#3a3a3a;
  --grey:#6b6b6b;
  --grey-mid:#9d9d9d;
  --line:#d6d6d6;
  --footer:#2f2f2f;
  --white:#ffffff;
}
*{box-sizing:border-box;margin:0;padding:0}
html,body{width:1200px;height:2365px;overflow:hidden}
body{position:relative;background:var(--white);font-family:"Lato",sans-serif;color:var(--ink)}
.heading{font-family:"Jost",sans-serif;font-weight:400;text-transform:uppercase;text-align:center;letter-spacing:.3px}

/* header */
.site-header{position:absolute;left:0;top:0;width:1200px;height:142px}
.brand{position:absolute;left:162px;top:40px;display:flex;align-items:center;gap:12px}
.brand-mark{width:22px;height:22px;background:var(--red)}
.brand-name{font-family:"Jost",sans-serif;font-weight:500;font-size:21px;color:var(--red);letter-spacing:1px}
.contact-strip{position:absolute;right:162px;top:35px;display:flex;gap:22px;font-size:15px;color:#333}
.contact-item{display:flex;align-items:center;gap:12px}
.icon-box{width:34px;height:30px;border:2px solid #777;display:flex;align-items:center;justify-content:center}
.main-nav{position:absolute;top:95px;left:498px;display:flex;gap:0}
.main-nav a{font-family:"Jost",sans-serif;font-size:14px;color:#222;text-decoration:none;text-transform:uppercase;position:absolute;white-space:nowrap}
.main-nav a.active{color:var(--red)}

/* hero */
.hero{position:absolute;left:0;top:142px;width:1200px;height:497px;
  background:linear-gradient(100deg,#5a3a22 0%,#7b5233 25%,#c9b8a0 45%,#8a5d3a 65%,#d8cdbd 85%,#6e4a2e 100%)}
.hero-caption{position:absolute;left:0;bottom:0;width:100%;height:56px;background:rgba(40,40,40,.55);
  color:var(--white);font-family:"Jost",sans-serif;font-weight:500;font-size:28px;text-align:center;line-height:56px;text-transform:uppercase}
.slide-arrow{position:absolute;top:208px;width:34px;height:34px;background:rgba(30,30,30,.75);display:flex;align-items:center;justify-content:center}

/* dividers */
.divider{position:absolute;height:14px}
.divider::before{content:"";position:absolute;left:0;right:0;top:6px;border-top:1px solid var(--line)}
.divider-mark{position:absolute;left:50%;top:0;transform:translateX(-50%);width:26px;height:14px;background:inherit;display:flex;justify-content:center;gap:3px;align-items:center}
.divider-mark i{display:block;width:3px;height:10px;background:var(--grey-mid);transform:skewX(-15deg)}

/* welcome */
.welcome-title{position:absolute;left:0;top:674px;width:1200px;font-size:33px;color:var(--grey)}
.welcome-title .accent{color:var(--red)}
.welcome-text{position:absolute;left:165px;top:746px;width:871px;font-size:13.5px;line-height:24px;text-align:center;color:#444}
.btn{position:absolute;border:2px solid #777;padding:3px;}
.btn span{display:flex;align-items:center;justify-content:center;gap:10px;height:100%;background:#6e6e6e;color:var(--white);font-size:13px;font-weight:700}

/* gallery */
.gallery{position:absolute;left:0;top:951px;width:1200px;height:634px}
.gallery-bg{position:absolute;inset:0;background:linear-gradient(180deg,#2d2d2d 0%,#262a25 45%,#141813 100%)}
.gallery-title{position:absolute;left:0;top:36px;width:1200px;font-size:31px;color:var(--white)}
.gallery-sub{position:absolute;left:0;top:127px;width:1200px;text-align:center;font-size:13.5px;color:#eee}
.gallery-grid{position:absolute;left:162px;top:173px;width:876px;display:grid;grid-template-columns:repeat(4,1fr);gap:6px}
.tile{position:relative;height:170px}
.tile-overlay{position:absolute;inset:0;background:rgba(255,255,255,.78);text-align:center}
.tile-overlay h3{font-family:"Jost",sans-serif;font-weight:500;font-size:24px;color:var(--red);margin-top:62px}
.tile-overlay p{font-size:11.5px;line-height:14px;color:#555;padding:4px 34px 0}

/* testimonials */
.testi-title{position:absolute;left:0;top:1626px;width:1200px;font-size:33px;color:var(--grey)}
.testi-title .accent{color:var(--red)}
.testi-card{position:absolute;top:1779px;width:276px;height:189px;border:1px solid #ddd;text-align:center}
.quote-badge{position:absolute;left:50%;top:-44px;transform:translateX(-50%);width:88px;height:88px;border-radius:50%;background:#6b6b6b;border:4px solid var(--white);box-shadow:0 0 0 1px #ddd;display:flex;align-items:center;justify-content:center}
.testi-name{margin-top:56px;font-family:"Jost",sans-serif;font-size:16px;color:var(--red)}
.stars{color:var(--red);font-size:12px;letter-spacing:3px;margin-top:2px}
.testi-text{font-size:12px;line-height:20px;color:#555;padding:6px 18px 0}
.more-btn{position:absolute;left:50%;bottom:-1px;transform:translateX(-50%);width:40px;height:20px;border-radius:20px 20px 0 0;background:#333;color:var(--white);font-size:16px;font-weight:700;line-height:22px}
.dots{position:absolute;top:1996px;left:575px;display:flex;gap:6px}
.dots i{width:7px;height:7px;border-radius:50%;border:1px solid #999}
.dots i.on{background:var(--red);border-color:var(--red)}

/* footer */
.site-footer{position:absolute;left:0;top:2050px;width:1200px;height:271px;background:var(--footer);color:#ddd}
.footer-col{position:absolute;top:36px}
.footer-col h4{font-family:"Jost",sans-serif;font-weight:400;font-size:19px;color:var(--white);text-transform:uppercase;padding-bottom:12px;border-bottom:1px solid #444;margin-bottom:14px}
.quick-links li{list-style:none;font-size:12px;margin-bottom:16px;padding-left:12px;position:relative}
.quick-links li::before{content:"";position:absolute;left:0;top:6px;width:4px;height:4px;background:#ddd;border-radius:50%}
.contact-list li{list-style:none;display:flex;gap:10px;font-size:12px;line-height:17px;margin-bottom:14px}
.contact-list strong{color:var(--white)}
.col-rule{position:absolute;top:40px;width:1px;height:170px;background:#444}
.map{position:absolute;left:621px;top:88px;width:417px;height:139px;border:3px solid var(--white);
  background:linear-gradient(135deg,#b8d4e8 0%,#cfe0c2 40%,#e9e5d6 60%,#a9cbe3 100%)}
.bottom-bar{position:absolute;left:0;top:2321px;width:1200px;height:44px;background:var(--red-bar);color:var(--white);font-size:12px}
.bottom-bar p{position:absolute;left:162px;top:14px}
.social{position:absolute;right:162px;top:10px;display:flex;gap:6px}
.social i{width:24px;height:24px;border:1px solid rgba(255,255,255,.8)}
</style>
</head>
<body>

<header class="site-header">
  <div class="brand"><span class="brand-mark"></span><span class="brand-name">DOVIN PRATCHELL HOMES</span></div>
  <div class="contact-strip">
    <div class="contact-item"><span class="icon-box"><svg width="16" height="16" viewBox="0 0 16 16"><path d="M3 1l3 3-1.5 2c1 2 3 4 5 5L11.5 9.5l3 3L13 15C7 15 1 9 1 3z" fill="#9b0f14"/></svg></span>608 555 0147</div>
    <div class="contact-item"><span class="icon-box"><svg width="18" height="13" viewBox="0 0 18 13"><rect width="18" height="13" fill="#9b0f14"/><path d="M0 0l9 7 9-7" fill="none" stroke="#fff" stroke-width="1.5"/></svg></span>hello@dovinpratchellhomes.com</div>
  </div>
  <nav class="main-nav">
    <a class="active" href="#" style="left:0">Home</a>
    <a href="#" style="left:90px">About Us</a>
    <a href="#" style="left:205px">Gallery</a>
    <a href="#" style="left:309px">Testimonials</a>
    <a href="#" style="left:451px">Contact Us</a>
  </nav>
</header>

<section class="hero" role="img" aria-label="Photo of a finished custom kitchen with wood cabinets, granite island and bar stools">
  <span class="slide-arrow" style="left:4px"><svg width="10" height="12"><path d="M8 0L1 6l7 6z" fill="#fff"/></svg></span>
  <span class="slide-arrow" style="right:4px"><svg width="10" height="12"><path d="M2 0l7 6-7 6z" fill="#fff"/></svg></span>
  <div class="hero-caption">We are a custom home builder in Wisconsin, USA</div>
</section>

<h2 class="heading welcome-title"><span class="accent">Welcome to Dovin</span> Pratchell Homes</h2>
<div class="divider" style="left:310px;top:720px;width:581px;background:#fff"><span class="divider-mark"><i></i><i></i><i></i></span></div>
<p class="welcome-text">Sed ut perspiciatis unde omnis iste natus error sit voluptatem accusantium doloremque laudantium, totam rem aperiam, eaque ipsa quae ab illo inventore veritatis et quasirrwtu architecto beatae vitae dicta sunt explicabo. Nemo enim ipsam voluptatem quia voluptas sit aspernatur aut odit aut fugit, sed quia consequuntur magninie dolores eos qui ratione voluptatem sequi nesciunt. Neque porro quisquam est, quie dolorem ipsum quia dolor sit amet, consectetur, adipisci velit, sed quia non numquam eius modi tempora incidunt uter labore et dolore .</p>
<a class="btn" style="left:539px;top:866px;width:120px;height:40px"><span>Read More <b>&raquo;</b></span></a>

<section class="gallery">
  <div class="gallery-bg" role="img" aria-label="Darkened photo of a house exterior at dusk"></div>
  <h2 class="heading gallery-title">Project Gallery</h2>
  <div class="divider" style="left:446px;top:84px;width:311px;background:#282828"><span class="divider-mark"><i style="background:#ccc"></i><i style="background:#ccc"></i><i style="background:#ccc"></i></span></div>
  <p class="gallery-sub">Sed ut perspiciatis unde omnis iste natus error sit voSed ut perspiciatis unde omnis iste natus error sit vo</p>
  <div class="gallery-grid">
    <div class="tile" role="img" aria-label="Bright white kitchen project photo" style="background:linear-gradient(135deg,#e8e2d8,#c9b9a3)">
      <div class="tile-overlay">
        <svg width="34" height="34" viewBox="0 0 34 34" style="position:absolute;left:88px;top:18px" fill="none" stroke="#777" stroke-width="2"><path d="M2 12V2h10M2 2l11 11M32 12V2H22M32 2L21 13M2 22v10h10M2 32l11-11M32 22v10H22M32 32L21 21"/></svg>
        <h3>MAPLE</h3>
        <p>Duis autem vel eum iriure dolor in hendrerit morein vulputate.</p>
      </div>
    </div>
    <div class="tile" role="img" aria-label="Kitchen and mudroom project photo" style="background:linear-gradient(135deg,#8a6a4a,#c8b89c)"></div>
    <div class="tile" role="img" aria-label="Living room with fireplace project photo" style="background:linear-gradient(135deg,#a8b4b8,#8a7058)"></div>
    <div class="tile" role="img" aria-label="Family room project photo" style="background:linear-gradient(135deg,#c8b89a,#7a4a38)"></div>
    <div class="tile" role="img" aria-label="Tiled fireplace with wood mantel project photo" style="background:linear-gradient(135deg,#b88a50,#5a3a22)"></div>
    <div class="tile" role="img" aria-label="Backyard deck project photo" style="background:linear-gradient(180deg,#d8d8cc,#8a5a48)"></div>
    <div class="tile" role="img" aria-label="Wood kitchen with dining chairs project photo" style="background:linear-gradient(135deg,#a86a38,#5a341c)"></div>
    <div class="tile" role="img" aria-label="White bathroom vanity project photo" style="background:linear-gradient(135deg,#e6e6e0,#a8a8a0)"></div>
  </div>
  <a class="btn" style="left:549px;top:548px;width:101px;height:37px"><span>View All <b>&raquo;</b></span></a>
</section>

<h2 class="heading testi-title"><span class="accent">What our</span> customer say</h2>
<div class="divider" style="left:370px;top:1674px;width:461px;background:#fff"><span class="divider-mark"><i></i><i></i><i></i></span></div>

<div class="testi-card" style="left:162px">
  <div class="quote-badge"><svg width="30" height="24" viewBox="0 0 30 24" fill="#fff"><path d="M0 0h12v12l-5 12H2l4-12H0zM17 0h12v12l-5 12h-5l4-12h-6z"/></svg></div>
  <div class="testi-name">Renata Colwell</div><div class="stars">★★★★★</div>
  <p class="testi-text">Duis autem vel eum iriure dolor in hendrerit in vulputate velit esse molestie conat vero eros et accumsan et iusto.</p>
  <div class="more-btn">+</div>
</div>
<div class="testi-card" style="left:462px">
  <div class="quote-badge"><svg width="30" height="24" viewBox="0 0 30 24" fill="#fff"><path d="M0 0h12v12l-5 12H2l4-12H0zM17 0h12v12l-5 12h-5l4-12h-6z"/></svg></div>
  <div class="testi-name">Damon Reyes</div><div class="stars">★★★★★</div>
  <p class="testi-text">Duis autem vel eum iriure dolor in hendrerit in vulputate velit esse molestie conat vero eros et accumsan et iusto.</p>
  <div class="more-btn">+</div>
</div>
<div class="testi-card" style="left:762px">
  <div class="quote-badge"><svg width="30" height="24" viewBox="0 0 30 24" fill="#fff"><path d="M0 0h12v12l-5 12H2l4-12H0zM17 0h12v12l-5 12h-5l4-12h-6z"/></svg></div>
  <div class="testi-name">Bryce Oakhurst</div><div class="stars">★★★★★</div>
  <p class="testi-text">Duis autem vel eum iriure dolor in hendrerit in vulputate velit esse molestie conat vero eros et accumsan et iusto.</p>
  <div class="more-btn">+</div>
</div>
<div class="dots"><i></i><i></i><i class="on"></i><i></i></div>

<footer class="site-footer">
  <div class="footer-col" style="left:162px;width:125px">
    <h4>Quick Links</h4>
    <ul class="quick-links"><li>Home</li><li>About Us</li><li>Gallery</li><li>Testimonials</li><li>Contact Us</li></ul>
  </div>
  <span class="col-rule" style="left:307px"></span>
  <div class="footer-col" style="left:353px;width:197px">
    <h4>Contact Details</h4>
    <ul class="contact-list">
      <li><svg width="12" height="16" viewBox="0 0 12 16"><path d="M6 0a6 6 0 0 1 6 6c0 4-6 10-6 10S0 10 0 6a6 6 0 0 1 6-6z" fill="#c4161c"/><circle cx="6" cy="6" r="2" fill="#2f2f2f"/></svg><span><strong>DOVIN PRATCHELL HOMES</strong><br>4820 Larchmont Road,<br>Verona, WI 53593</span></li>
      <li><svg width="12" height="12" viewBox="0 0 16 16"><path d="M3 1l3 3-1.5 2c1 2 3 4 5 5L11.5 9.5l3 3L13 15C7 15 1 9 1 3z" fill="#c4161c"/></svg>608 555 0147</li>
      <li><svg width="12" height="12" viewBox="0 0 16 16"><path d="M3 1l3 3-1.5 2c1 2 3 4 5 5L11.5 9.5l3 3L13 15C7 15 1 9 1 3z" fill="#c4161c"/></svg>608 555 0147</li>
      <li><svg width="13" height="10" viewBox="0 0 18 13"><rect width="18" height="13" fill="#c4161c"/><path d="M0 0l9 7 9-7" fill="none" stroke="#2f2f2f" stroke-width="1.5"/></svg>hello@dovinpratchellhomes.com</li>
    </ul>
  </div>
  <span class="col-rule" style="left:582px"></span>
  <div class="footer-col" style="left:621px;width:417px">
    <h4>Location Map</h4>
  </div>
  <div class="map" role="img" aria-label="Location map showing the office"></div>
</footer>

<div class="bottom-bar">
  <p>Copyright © 2017 Dovin Pratchell Homes. All Rights Reserved.</p>
  <div class="social"><i></i><i></i><i></i><i></i></div>
</div>

</body>
</html>
```